Hello,
Corinne Haskett Equestrian needs a business card. We are a high performance show jumping stables based at Willowmere Reserve in morningotn. We pride ourselves on producing high quality show jumping horses and competing our stock at a high level. My business card need to have my logo on it, and i would like it to have a classic design with a modern touch. I would like it to have quite a natural feel about it. It needs to be in a font which is easy to read as I spend a lot of time competing internationally and overseas, and i need to be able to give it out to breeders and contacts where English isnt their first language. I will need it to include the following details:
-Corinne Haskett Equestrian
-Based at Willowmere Reserve Mornington
-Address: 17 Tremont Lane Mornington Victoria 3931
-Mobile number: 0412605948
- website: www.corinnehaskettequestrian.example
Target Market(s)
For business adults who english may not be their first language
Industry/Entity Type
Business

```html
<!DOCTYPE html>
<html lang="en">
<head>
<meta charset="utf-8">
<title>Corinne Haskett Equestrian – Business Card</title>
<link rel="stylesheet" href="https://fonts.googleapis.com/css2?family=Cinzel:wght@400&family=Merriweather:wght@700&display=swap">
<style>
  :root {
    --page-bg: #ffffff;
    --card-white: #ffffff;
    --saddle-brown: #a45b25;
    --ink: #2a2a2a;
    --label-grey: #a3a3a3;
    --card-shadow: rgba(0, 0, 0, 0.22);
  }
  html, body {
    margin: 0;
    padding: 0;
    overflow: hidden;
  }
  body {
    width: 1200px;
    height: 1000px;
    background: var(--page-bg);
    position: relative;
  }
  .side-label {
    position: absolute;
    left: 60px;
    width: 270px;
    text-align: center;
    font-family: Arial, Helvetica, sans-serif;
    font-size: 36px;
    color: var(--label-grey);
    line-height: 1;
  }
  .side-label--front { top: 258px; }
  .side-label--back { top: 706px; }

  .card {
    position: absolute;
    left: 393px;
    width: 672px;
    height: 432px;
    box-shadow: 6px 8px 10px var(--card-shadow);
  }
  .card--front {
    top: 40px;
    background: var(--card-white);
    border: 1px solid #ececec;
    box-sizing: border-box;
  }
  .card--back {
    top: 533px;
    background: var(--saddle-brown);
  }

  .brand-name {
    position: absolute;
    left: 0;
    width: 100%;
    text-align: center;
    font-family: "Cinzel", Georgia, serif;
    font-weight: 400;
    font-size: 34px;
    letter-spacing: 1px;
    line-height: 1;
  }
  .card--front .brand-name { top: 132px; color: var(--ink); }
  .card--back .brand-name { top: 170px; color: var(--card-white); }

  .based-at {
    position: absolute;
    top: 274px;
    left: 0;
    width: 100%;
    text-align: center;
    font-family: "Merriweather", Georgia, serif;
    font-weight: 700;
    font-size: 22px;
    color: var(--saddle-brown);
    line-height: 1;
  }
  .contact-frame {
    position: absolute;
    left: 0;
    top: 0;
    width: 672px;
    height: 432px;
  }
  .contact-line {
    position: absolute;
    left: 0;
    width: 100%;
    text-align: center;
    font-family: "Merriweather", Georgia, serif;
    font-weight: 700;
    font-size: 19px;
    color: var(--ink);
    line-height: 1;
  }
  .contact-line--address { top: 328px; }
  .contact-line--mobile { top: 360px; }

  .website {
    position: absolute;
    top: 280px;
    left: 0;
    width: 100%;
    text-align: center;
    font-family: "Merriweather", Georgia, serif;
    font-weight: 700;
    font-size: 21px;
    color: var(--card-white);
    line-height: 1;
  }
</style>
</head>
<body>
  <div class="side-label side-label--front">Front side</div>
  <div class="side-label side-label--back">Back side</div>

  <section class="card card--front" aria-label="Business card front">
    <div class="brand-name">Corinne Haskett Equestrian</div>
    <div class="based-at">Based at Willowmere Reserve Mornington</div>
    <svg class="contact-frame" viewBox="0 0 672 432" aria-hidden="true">
      <path d="M35 370 L35 316 Q336 292 637 316 L637 370 L512 370 M162 370 L35 370"
            fill="none" stroke="#2a2a2a" stroke-width="2"/>
    </svg>
    <div class="contact-line contact-line--address">Address: 17 Tremont Lane Mornington Victoria 3931</div>
    <div class="contact-line contact-line--mobile">Mobile number: 0412605948</div>
  </section>

  <section class="card card--back" aria-label="Business card back">
    <div class="brand-name">Corinne Haskett Equestrian</div>
    <div class="website">www.corinnehaskettequestrian.example</div>
  </section>
</body>
</html>
```